TARNVALE EV

We need a business card design for a new Luxury golf cart Company Tarnvale. We manufacture and sell high end golf carts. We would like to see designs that are high end. I have the logo so really need a nice clean look.

```html
<!DOCTYPE html>
<html lang="en">
<head>
<meta charset="utf-8">
<title>Tarnvale EV – Business Card</title>
<link rel="stylesheet" href="https://fonts.googleapis.com/css2?family=Chakra+Petch:wght@400;600;700&display=swap">
<style>
  :root {
    --canvas-bg: #ececec;
    --card-bg: #0a0a0a;
    --silver: #cfd3d6;
    --white: #ffffff;
    --text-soft: #e6e6e6;
    --accent: #0f7d66;
    --brand-font: "Chakra Petch", sans-serif;
  }
  * { box-sizing: border-box; margin: 0; padding: 0; }
  html, body {
    width: 1200px;
    height: 1200px;
    overflow: hidden;
    background: var(--canvas-bg);
    font-family: var(--brand-font);
  }
  .canvas { position: relative; width: 1200px; height: 1200px; }

  .card {
    position: absolute;
    left: 155px;
    width: 888px;
    height: 520px;
    background: var(--card-bg);
    box-shadow: 0 2px 6px rgba(0,0,0,0.18);
  }
  .card--front { top: 61px; }
  .card--back { top: 611px; }

  .wordmark {
    position: absolute;
    left: 0;
    width: 100%;
    text-align: center;
    font-family: var(--brand-font);
    font-weight: 700;
    color: var(--silver);
    line-height: 1;
    white-space: nowrap;
  }
  .card--front .wordmark { top: 100px; font-size: 76px; letter-spacing: 2px; }
  .card--back .wordmark { top: 205px; font-size: 110px; letter-spacing: 3px; }

  .holder-name {
    position: absolute;
    top: 260px;
    width: 100%;
    text-align: center;
    font-weight: 700;
    font-size: 38px;
    color: var(--white);
    letter-spacing: 1px;
    line-height: 1;
  }
  .holder-role {
    position: absolute;
    top: 304px;
    width: 100%;
    text-align: center;
    font-weight: 400;
    font-size: 17px;
    color: var(--text-soft);
    letter-spacing: 0.5px;
  }

  .contact-icon {
    position: absolute;
    top: 373px;
    width: 30px;
    height: 30px;
    margin-left: -15px;
  }
  .contact-icon--phone { left: 218px; }
  .contact-icon--mail { left: 445px; }
  .contact-icon--web { left: 666px; }

  .contact-line {
    position: absolute;
    top: 428px;
    width: 100%;
    display: flex;
    justify-content: center;
    align-items: center;
    gap: 30px;
    font-size: 22px;
    font-weight: 400;
    color: var(--text-soft);
    letter-spacing: 1px;
    white-space: nowrap;
  }
  .contact-divider { color: var(--text-soft); }
</style>
</head>
<body>
<main class="canvas">

  <section class="card card--front" aria-label="Business card front">
    <div class="wordmark">TARNVALE</div>

    <h1 class="holder-name">Daniel Hart</h1>
    <p class="holder-role">Founder</p>

    <svg class="contact-icon contact-icon--phone" viewBox="0 0 24 24" aria-hidden="true">
      <path fill="var(--accent)" d="M6.6 10.8c1.4 2.8 3.8 5.1 6.6 6.6l2.2-2.2c.3-.3.7-.4 1-.2 1.1.4 2.3.6 3.6.6.6 0 1 .4 1 1V20c0 .6-.4 1-1 1C10.6 21 3 13.4 3 4c0-.6.4-1 1-1h3.5c.6 0 1 .4 1 1 0 1.3.2 2.5.6 3.6.1.3 0 .7-.2 1z"/>
    </svg>
    <svg class="contact-icon contact-icon--mail" viewBox="0 0 24 24" aria-hidden="true">
      <rect x="2" y="4.5" width="20" height="15" rx="1.5" fill="var(--accent)"/>
      <path d="M3.5 6.5 12 12.5l8.5-6" fill="none" stroke="var(--card-bg)" stroke-width="1.6"/>
    </svg>
    <svg class="contact-icon contact-icon--web" viewBox="0 0 24 24" aria-hidden="true">
      <g fill="none" stroke="var(--accent)" stroke-width="1.5">
        <circle cx="12" cy="12" r="9.5"/>
        <ellipse cx="12" cy="12" rx="4.2" ry="9.5"/>
        <line x1="2.5" y1="12" x2="21.5" y2="12"/>
        <path d="M4.2 7h15.6M4.2 17h15.6"/>
      </g>
    </svg>

    <div class="contact-line">
      <span class="contact-phone">041 3659 0000</span>
      <span class="contact-divider">|</span>
      <span class="contact-email">info@tarnvale.net</span>
      <span class="contact-divider">|</span>
      <span class="contact-web">www.tarnvale.net</span>
    </div>
  </section>

  <section class="card card--back" aria-label="Business card back">
    <div class="wordmark">TARNVALE</div>
  </section>

</main>
</body>
</html>
```